New Modern floristry business design

Hi, we are a new business based in Sydney called "copper fern floristry"

With so many floristry's we need a good design that will set a great first impression.

A few descriptive words on how we envision copper fern floristry:

-dynamic design
-minimal colour (colour can be used to enhance the design)
-black white grey (can include gold,silver,metallic shadowing)
Strong "COPPER FERN" with a classy "FLORISTRY"
Bold with a touch of feminine

Copper Fern Floristry,
Delia Varnet,
Copperfernfloristry@mailbay.com.au

```html
<!DOCTYPE html>
<html lang="en">
<head>
<meta charset="utf-8">
<title>Copper Fern Floristry – Business Card</title>
<link rel="stylesheet" href="https://fonts.googleapis.com/css2?family=Marck+Script&display=swap">
<style>
  :root {
    --stage: #808080;
    --card: #121212;
    --gold: #e8bd2c;
    --silver: #ececec;
    --vine: rgba(70, 70, 70, 0.55);
    --petal: rgba(232, 189, 44, 0.28);
  }
  * { margin: 0; padding: 0; box-sizing: border-box; }
  html, body {
    width: 1200px;
    height: 1000px;
    overflow: hidden;
    background: var(--stage);
  }
  .card {
    position: absolute;
    left: 210px;
    width: 781px;
    height: 480px;
    background: var(--card);
    overflow: hidden;
    font-family: "Marck Script", cursive;
  }
  .card--front { top: 10px; }
  .card--back { top: 510px; }

  .vine-flourish {
    position: absolute;
    border-radius: 50%;
    background: radial-gradient(ellipse at center, var(--vine) 0%, rgba(40, 40, 40, 0.25) 55%, transparent 75%);
  }
  .card--front .vine-flourish { left: 0; top: 150px; width: 781px; height: 210px; }
  .card--back .vine-flourish { left: 0; top: 60px; width: 781px; height: 330px; }

  .petal-scatter {
    position: absolute;
    left: 170px;
    top: 270px;
    width: 420px;
    height: 150px;
    border-radius: 50%;
    background: radial-gradient(ellipse at center, var(--petal) 0%, transparent 70%);
  }

  .business-name {
    position: absolute;
    left: 0;
    width: 100%;
    text-align: center;
    color: var(--gold);
    font-weight: 400;
    white-space: nowrap;
  }
  .card--front .business-name { top: 82px; font-size: 56px; }
  .card--back .business-name { top: 178px; font-size: 70px; }

  .person-name {
    position: absolute;
    left: 0;
    width: 100%;
    top: 218px;
    text-align: center;
    font-size: 56px;
    color: var(--silver);
    white-space: nowrap;
  }
  .contact-email {
    position: absolute;
    right: 60px;
    top: 370px;
    font-size: 27px;
    color: var(--silver);
    white-space: nowrap;
  }
</style>
</head>
<body>
  <section class="card card--front">
    <div class="vine-flourish" role="img" aria-label="Faint grey decorative vine with leaves sweeping across the card"></div>
    <h1 class="business-name">Copper Fern Floristry</h1>
    <p class="person-name">Delia Varnet</p>
    <p class="contact-email">Copperfernfloristry@mailbay.com.au</p>
  </section>

  <section class="card card--back">
    <div class="vine-flourish" role="img" aria-label="Faint grey decorative vine with leaves sweeping across the card"></div>
    <div class="petal-scatter" role="img" aria-label="Scattered golden petals falling beneath the business name"></div>
    <h2 class="business-name">Copper Fern Floristry</h2>
  </section>
</body>
</html>
```